BRAMLEIGH real estate family office

Hello, Our business is a real estate intermediation activity on high-end goods (amounts exceeding € 10m) for corporate and private clients. You can see our logo on the site www.bramleigh-invented.fr We would like to keep that spirit with the hexagon that represents France (transactions between Monaco and Saint Tropez, Courchevel and Paris). And the "baseline" that is "real estate family office". The corporate logo should be and can be printed by embossing (relief). We must integrate the name, first name, phone, email and website. Finally, to imbibe the spirit of business, here is a detail of the activity. "Genuine consulting firm in real estate investments, BRAMLEIGH works with its customers as a specialized player in the high-end markets, we are recognized for our ultra-confidential approach and tailor-made, as well as the quality of our network. We broadcast any information on the market and we work exclusively through a strong relationship we have developed over the years. BRAMLEIGH is active on the French Riviera (from Monaco to Saint-Tropez), the Alps (Courchevel, Méribel, Megève) and Paris (essentially market premium). Always looking for opportunities for our clients, we work on two investment areas: residential luxury real estate (properties, vineyards, mansions, land, etc.) commercial real estate (empty office buildings or yield, hotel properties, land, etc.) "

Target Market(s)

High foreign end customers. corporate and private.

Industry/Entity Type

Real Estate

Contact Information for Business Card

LOGO
baseline
Laurent Dufossé
+33(0)6.41.57.09.64
ld@bramleigh-invented.fr
www.bramleigh-invented.fr

Font styles to use
Serif

Colors
cedeed
0255a3
3277b5
85abd2
85cae6
34a7d7
0792cd
cfdeed
1b1b1b

Requirements
Must have
• see description

```html
<!DOCTYPE html>
<html lang="en">
<head>
<meta charset="utf-8">
<title>Bramleigh – business cards</title>
<link href="https://fonts.googleapis.com/css2?family=Questrial&family=Arimo:wght@400&display=swap" rel="stylesheet">
<style>
  :root {
    --page: #e8e5e0;
    --card: #fbfbfb;
    --card-shade: #eeeeee;
    --stripe: #a3a5a9;
    --blue-deep: #2a4fae;
    --blue-light: #4f7bcb;
    --wordmark: #8a8c90;
    --baseline: #4f6cc0;
    --mark: #2f56b0;
    --white: #ffffff;
  }
  * { margin: 0; padding: 0; box-sizing: border-box; }
  html, body { width: 1200px; height: 858px; overflow: hidden; }
  body {
    background: var(--page);
    display: flex;
    align-items: center;
    justify-content: center;
    gap: 40px;
    font-family: "Questrial", sans-serif;
  }
  .card {
    width: 540px;
    height: 309px;
    background: linear-gradient(135deg, var(--card) 40%, var(--card-shade));
    box-shadow: 0 10px 24px rgba(0,0,0,.18), 0 2px 4px rgba(0,0,0,.12);
    position: relative;
    overflow: hidden;
  }

  /* shared logo lockup */
  .logo { display: inline-flex; flex-direction: column; align-items: flex-end; }
  .logo-line { display: flex; align-items: center; gap: 14px; }
  .logo-square { width: 22px; height: 22px; background: var(--mark); }
  .logo-name {
    color: var(--wordmark);
    font-size: 46px;
    letter-spacing: 6px;
    line-height: 1;
  }
  .logo-baseline {
    color: var(--baseline);
    font-size: 15px;
    letter-spacing: 1.5px;
    margin-top: 6px;
  }

  /* front */
  .front-top {
    height: 132px;
    display: flex;
    align-items: center;
    padding-left: 38px;
  }
  .front-stripe { height: 12px; background: var(--stripe); }
  .front-band {
    height: 165px;
    background: linear-gradient(100deg, var(--blue-deep), var(--blue-light) 60%, var(--blue-deep));
    display: flex;
    align-items: center;
    color: var(--white);
    font-family: "Arimo", sans-serif;
  }
  .holder-name {
    width: 250px;
    padding-left: 36px;
    font-size: 23px;
    align-self: flex-end;
    padding-bottom: 34px;
  }
  .divider { width: 1.5px; height: 104px; background: var(--white); opacity: .9; }
  .contacts { list-style: none; padding-left: 26px; }
  .contacts li {
    display: flex;
    align-items: center;
    gap: 12px;
    font-size: 14px;
    line-height: 1;
    margin: 12px 0;
  }
  .contact-icon { width: 16px; height: 16px; flex: none; }

  /* back */
  .back {
    display: flex;
    align-items: center;
    justify-content: center;
  }
  .back .logo-name { font-size: 52px; }
  .back .logo-square { width: 26px; height: 26px; }
  .back .logo-baseline { font-size: 17px; }
</style>
</head>
<body>

  <section class="card front">
    <div class="front-top">
      <div class="logo">
        <div class="logo-line">
          <span class="logo-square"></span>
          <span class="logo-name">BRAMLEIGH</span>
        </div>
        <span class="logo-baseline">real estate family office</span>
      </div>
    </div>
    <div class="front-stripe"></div>
    <div class="front-band">
      <p class="holder-name">Laurent Dufossé</p>
      <span class="divider"></span>
      <ul class="contacts">
        <li>
          <svg class="contact-icon" viewBox="0 0 16 16" aria-hidden="true">
            <rect width="16" height="16" fill="#fff"/>
            <path d="M4.5 3.5l2 2-1 1.2c.6 1.4 1.6 2.4 3 3l1.2-1 2 2-1.2 1.6C7 12 4 9 3 4.7z" fill="#2a4fae"/>
          </svg>
          <span>+33(0)6.41.57.09.64</span>
        </li>
        <li>
          <svg class="contact-icon" viewBox="0 0 16 16" aria-hidden="true">
            <rect width="16" height="16" fill="#fff"/>
            <circle cx="8" cy="8" r="4.6" fill="none" stroke="#2a4fae" stroke-width="1.2"/>
            <path d="M3.4 8h9.2M8 3.4c-2 2.6-2 6.6 0 9.2M8 3.4c2 2.6 2 6.6 0 9.2" fill="none" stroke="#2a4fae" stroke-width="1"/>
          </svg>
          <span>www.bramleigh-invented.fr</span>
        </li>
        <li>
          <svg class="contact-icon" viewBox="0 0 16 16" aria-hidden="true">
            <rect width="16" height="16" fill="#fff"/>
            <rect x="3" y="4.5" width="10" height="7" fill="none" stroke="#2a4fae" stroke-width="1.2"/>
            <path d="M3 4.5l5 4 5-4" fill="none" stroke="#2a4fae" stroke-width="1.2"/>
          </svg>
          <span>ld@bramleigh-invented.fr</span>
        </li>
      </ul>
    </div>
  </section>

  <section class="card back">
    <div class="logo">
      <div class="logo-line">
        <span class="logo-square"></span>
        <span class="logo-name">BRAMLEIGH</span>
      </div>
      <span class="logo-baseline">real estate family office</span>
    </div>
  </section>

</body>
</html>
```